6 Product labels for a Skincare brand

I have a logo and 6 label templates for 6 skincare productsI need someone to design the product labelsthe design of all 6 labels should be very similar just with basic adjustmentsPlease show me only the design for "Velaquin30ml_Template_V2" and then we can do the others

Target Market(s)

Women +45

Industry/Entity Type

Skin Care Product

Font styles to use
Other font styles liked:
• Helvetica

Colors
ffffff
fef7ee
feeeee
fbe7d2
fefced

Requirements
Must have
• Clean Clean design
• Company details are:
• Distributed by: MARLEE QUINTAV, Denver, CO 80000
• support@marleequintav.example, (866) 555-0172

```html
<!DOCTYPE html>
<html lang="en">
<head>
<meta charset="utf-8">
<title>Velaquin 30ml Label Variations</title>
<link href="https://fonts.googleapis.com/css2?family=Mulish:wght@400;600;700&family=Josefin+Sans:wght@400&family=Marcellus&family=Oswald:wght@300&family=Yellowtail&display=swap" rel="stylesheet">
<style>
:root{
  --page:#ffffff;
  --peach-bg:#f8e0cb;
  --peach-ink:#7a2a22;
  --peach-arch:#f0c9a6;
  --peach-band:#e2ac88;
  --cream-bg:#fbedc8;
  --cream-ink:#3f6b73;
  --gold:#d9b56a;
  --leaf-blue:#8fb3b8;
  --linen-bg:#f3f3ef;
  --linen-ink:#52683f;
  --leaf-green:#7d9567;
  --mark:#2b2b2b;
  --border:#4a4a4a;
}
*{margin:0;padding:0;box-sizing:border-box}
html,body{width:1200px;height:538px;overflow:hidden;background:var(--page)}
body{position:relative;font-family:"Mulish",Arial,sans-serif}
.label{position:absolute;left:23px;width:1154px;height:144px;color:var(--ink)}
.label--peach{top:19px;background:var(--peach-bg);--ink:var(--peach-ink)}
.label--cream{top:188px;background:var(--cream-bg);--ink:var(--cream-ink)}
.label--linen{top:359px;background:var(--linen-bg);--ink:var(--linen-ink);border:1px solid var(--border);border-radius:3px}
.info{position:absolute;left:17px;top:16px;width:288px;font-size:8.2px;line-height:11px;text-align:justify;text-transform:uppercase}
.info p{margin-bottom:7px}
.info strong{font-weight:700}
.distributor{position:absolute;left:17px;top:99px;font-size:8.2px;line-height:11px;white-space:nowrap}
.distributor strong{font-weight:700}
.distributor .indent{padding-left:73px;display:block}
.lot{position:absolute;left:262px;top:103px;font-size:7px;font-weight:700}
.lot-box{position:absolute;left:262px;top:112px;width:52px;height:17px;border:1px solid var(--ink);background:#fff}
.ingredients{position:absolute;left:723px;top:16px;width:411px;font-size:8.2px;line-height:11.2px;text-align:justify}
.ingredients strong{font-weight:700}
.certified{position:absolute;right:20px;top:120px;font-size:8.5px}
.brand{position:absolute;left:424px;width:200px;text-align:center;font-family:"Josefin Sans",sans-serif;color:var(--mark);font-size:16px;letter-spacing:6px;line-height:20px}
.brand-dot{display:block;width:6px;height:6px;border-radius:50%;background:var(--mark);margin:0 auto 6px}
.product{position:absolute;left:424px;width:200px;text-align:center;color:var(--ink)}
.size{position:absolute;font-size:9px;color:var(--ink);white-space:nowrap}
.art{position:absolute}
</style>
</head>
<body>

<section class="label label--peach">
  <div class="info">
    <p><strong>Directions:</strong> Apply evenly over the face and neck. Use twice daily as part of your anti-aging regime or as needed for added moisture.</p>
    <p><strong>Caution:</strong> For external use only. Avoid direct contact with eyes. If irritation occurs, discontinue use.</p>
  </div>
  <div class="distributor"><strong>DISTRIBUTED BY:</strong> MARLEE QUINTAV<span class="indent">DENVER, CO 80000</span>SUPPORT@MARLEEQUINTAV.EXAMPLE, (866) 555-0172</div>
  <div class="lot">T-V2</div><div class="lot-box"></div>
  <svg class="art" style="left:447px;top:0" width="155" height="134" viewBox="0 0 155 134">
    <path d="M1 0 V96 A36 36 0 0 0 37 132 H118 A36 36 0 0 0 154 96 V0" fill="var(--peach-arch)" stroke="#d9a07f" stroke-width="1"/>
    <rect x="1" y="90" width="153" height="22" fill="var(--peach-band)"/>
  </svg>
  <div class="art" role="img" aria-label="Faint pale leaf decoration" style="left:570px;top:20px;width:70px;height:120px;background:linear-gradient(160deg,rgba(255,255,255,.35),rgba(255,255,255,0));border-radius:70% 0 70% 0"></div>
  <div class="brand" style="top:24px"><span class="brand-dot"></span>MARLEE<br>QUINTAV</div>
  <div class="product" style="top:90px;font-family:'Marcellus',serif;font-size:17px;color:var(--peach-ink)">Velaquin</div>
  <div class="size" style="left:576px;top:122px;font-weight:700;font-size:9.5px">30 ml &nbsp;|&nbsp; 1 fl oz</div>
  <div class="ingredients"><strong>INGREDIENTS:</strong> Water, Prunus Amygdalus Dulcis (Sweet Almond) Oil, Caprylic/Capric Triglyceride, Myristic Acid, Stearic Acid, Cetyl Esters, Glyceryl Stearate SE, Aloe Barbadensis (Aloe Vera) Leaf Juice*, Cetearyl Alcohol, Ceteareth-20, Diheptyl Succinate, Capryloyl Glycerin/Sebacic Acid Copolymer, Pyrus Malus (Apple) Fruit Extract, Glycerin, Dehydroacetic Acid, Benzyl Alcohol, Saccharide Isomerate, Acetyl Hexapeptide-30, Arginine, Caprylyl Glycol, Tromethamine, Carbomer, Potassium Sorbate, Squalane, Tocopheryl Acetate, Ubiquinone, Fagus Sylvatica Bud Extract, Sodium Carboxymethyl Beta-Glucan, Taraxacum Officinale (Dandelion) Leaf Extract, Salvia Officinalis (Sage) Leaf Extract, Melissa Officinalis Leaf Extract, Sodium Benzoate, Citric Acid.</div>
  <div class="certified">*Certified Organic Ingredients</div>
</section>

<section class="label label--cream">
  <div class="info">
    <p><strong>Directions:</strong> Apply evenly over the face and neck. Use twice daily as part of your anti-aging regime or as needed for added moisture.</p>
    <p><strong>Caution:</strong> For external use only. Avoid direct contact with eyes. If irritation occurs, discontinue use.</p>
  </div>
  <div class="distributor"><strong>DISTRIBUTED BY:</strong> MARLEE QUINTAV<span class="indent">DENVER, CO 80000</span>SUPPORT@MARLEEQUINTAV.EXAMPLE, (866) 555-0172</div>
  <div class="lot">T-V2</div><div class="lot-box"></div>
  <svg class="art" style="left:430px;top:0" width="185" height="144" viewBox="0 0 185 144">
    <ellipse cx="92" cy="72" rx="78" ry="68" fill="#fdf5de" opacity=".8"/>
    <polygon points="40,2 150,4 182,62 140,144 40,142 8,72" fill="none" stroke="var(--gold)" stroke-width="1"/>
    <polygon points="60,0 170,20 176,100 110,144 20,120 14,40" fill="none" stroke="var(--gold)" stroke-width="1"/>
  </svg>
  <div class="art" role="img" aria-label="Watercolour blue leaves" style="left:437px;top:6px;width:50px;height:80px;background:linear-gradient(150deg,var(--leaf-blue),#c9dcd8);border-radius:80% 10% 80% 10%;opacity:.85"></div>
  <div class="brand" style="top:24px"><span class="brand-dot"></span>MARLEE<br>QUINTAV</div>
  <div class="product" style="top:92px;font-family:'Oswald',sans-serif;font-weight:300;font-size:17px;letter-spacing:1px">VELAQUIN</div>
  <div class="size" style="left:494px;top:122px">30 ml &nbsp;|&nbsp; 1 fl oz</div>
  <div class="ingredients"><strong>INGREDIENTS:</strong> Water, Prunus Amygdalus Dulcis (Sweet Almond) Oil, Caprylic/Capric Triglyceride, Myristic Acid, Stearic Acid, Cetyl Esters, Glyceryl Stearate SE, Aloe Barbadensis (Aloe Vera) Leaf Juice*, Cetearyl Alcohol, Ceteareth-20, Diheptyl Succinate, Capryloyl Glycerin/Sebacic Acid Copolymer, Pyrus Malus (Apple) Fruit Extract, Glycerin, Dehydroacetic Acid, Benzyl Alcohol, Saccharide Isomerate, Acetyl Hexapeptide-30, Arginine, Caprylyl Glycol, Tromethamine, Carbomer, Potassium Sorbate, Squalane, Tocopheryl Acetate, Ubiquinone, Fagus Sylvatica Bud Extract, Sodium Carboxymethyl Beta-Glucan, Taraxacum Officinale (Dandelion) Leaf Extract, Salvia Officinalis (Sage) Leaf Extract, Melissa Officinalis Leaf Extract, Sodium Benzoate, Citric Acid.</div>
  <div class="certified">*Certified Organic Ingredients</div>
</section>

<section class="label label--linen">
  <div class="info">
    <p><strong>Directions:</strong> Apply evenly over the face and neck. Use twice daily as part of your anti-aging regime or as needed for added moisture.</p>
    <p><strong>Caution:</strong> For external use only. Avoid direct contact with eyes. If irritation occurs, discontinue use.</p>
  </div>
  <div class="distributor"><strong>DISTRIBUTED BY:</strong> MARLEE QUINTAV<span class="indent">DENVER, CO 80000</span>SUPPORT@MARLEEQUINTAV.EXAMPLE, (866) 555-0172</div>
  <div class="lot">T-V2</div><div class="lot-box"></div>
  <div class="art" role="img" aria-label="Botanical illustration of a green leafy branch" style="left:383px;top:0;width:78px;height:38px;background:linear-gradient(100deg,#6f8458,#a9b893);border-radius:0 0 60% 40%"></div>
  <div class="art" role="img" aria-label="Botanical illustration of a flowering herb stem" style="left:590px;top:42px;width:72px;height:102px;background:linear-gradient(170deg,#b9c79f,var(--leaf-green));border-radius:50% 50% 10% 10%;opacity:.85"></div>
  <div class="brand" style="top:24px"><span class="brand-dot"></span>MARLEE<br>QUINTAV</div>
  <div class="product" style="top:86px;font-family:'Yellowtail',cursive;font-size:20px;color:var(--leaf-green)">Velaquin</div>
  <div class="size" style="left:494px;top:122px;color:#8a8a8a">30 ml &nbsp;|&nbsp; 1 fl oz</div>
  <div class="ingredients"><strong>INGREDIENTS:</strong> Water, Prunus Amygdalus Dulcis (Sweet Almond) Oil, Caprylic/Capric Triglyceride, Myristic Acid, Stearic Acid, Cetyl Esters, Glyceryl Stearate SE, Aloe Barbadensis (Aloe Vera) Leaf Juice*, Cetearyl Alcohol, Ceteareth-20, Diheptyl Succinate, Capryloyl Glycerin/Sebacic Acid Copolymer, Pyrus Malus (Apple) Fruit Extract, Glycerin, Dehydroacetic Acid, Benzyl Alcohol, Saccharide Isomerate, Acetyl Hexapeptide-30, Arginine, Caprylyl Glycol, Tromethamine, Carbomer, Potassium Sorbate, Squalane, Tocopheryl Acetate, Ubiquinone, Fagus Sylvatica Bud Extract, Sodium Carboxymethyl Beta-Glucan, Taraxacum Officinale (Dandelion) Leaf Extract, Salvia Officinalis (Sage) Leaf Extract, Melissa Officinalis Leaf Extract, Sodium Benzoate, Citric Acid.</div>
  <div class="certified">*Certified Organic Ingredients</div>
</section>

</body>
</html>
```